New Velbrix Business Card Design

We need a business card to match our new branding. The look should utilize the elements as attached here (Vector files & new exec overview are attached.) I really like 'organic' looking elements (e.g. an idea would be to have this printed on recycled paper stock). Thank you! Looking forward to seeing your designs.

Business

```html
<!DOCTYPE html>
<html lang="en">
<head>
<meta charset="utf-8">
<title>Velbrix Business Card</title>
<link href="https://fonts.googleapis.com/css2?family=PT+Sans:wght@400;700&display=swap" rel="stylesheet">
<style>
  :root {
    --bg: #e4e5e7;
    --paper: #ffffff;
    --green: #8cc43f;
    --blue: #1b6fb8;
    --ink: #4a4a4a;
    --shadow: rgba(0,0,0,0.14);
  }
  * { margin: 0; padding: 0; box-sizing: border-box; }
  html, body {
    width: 1200px; height: 800px; overflow: hidden;
    background: var(--bg);
    font-family: "PT Sans", sans-serif;
  }
  .stage {
    position: relative; width: 1200px; height: 800px;
    display: flex; align-items: center; justify-content: center; gap: 60px;
  }
  .card {
    position: relative; width: 525px; height: 300px;
    overflow: hidden; box-shadow: 0 10px 26px var(--shadow);
  }
  .card-front { background: var(--paper); }
  .card-back { background: var(--green); }
  .front-swoosh { position: absolute; left: 0; top: 0; }
  .holder {
    position: absolute; left: 44px; top: 168px; line-height: 1.1;
  }
  .holder-name { color: var(--blue); font-weight: 700; font-size: 15px; }
  .holder-title { color: var(--ink); font-size: 13px; }
  .brand {
    position: absolute; display: flex; align-items: center; gap: 8px;
    font-weight: 700; letter-spacing: 1px; line-height: 1;
  }
  .brand-dot { border-radius: 50%; flex: none; }
  .brand-front { right: 52px; top: 110px; font-size: 50px; color: var(--blue); }
  .brand-front .brand-dot { width: 22px; height: 22px; background: var(--green); }
  .contact {
    position: absolute; right: 52px; bottom: 26px; text-align: right;
    color: var(--ink); font-size: 12.5px; line-height: 1.35;
  }
  .contact-gap { height: 8px; }
  .contact-line { display: flex; align-items: center; justify-content: flex-end; gap: 6px; }
  .contact-icon { width: 11px; height: 11px; flex: none; }
  .contact-web { color: var(--blue); }
  .brand-back { left: 50%; top: 112px; transform: translateX(-50%); font-size: 56px; color: var(--paper); }
  .brand-back .brand-dot { width: 24px; height: 24px; background: var(--paper); }
  .back-web {
    position: absolute; left: 0; right: 0; top: 196px; text-align: center;
    color: var(--paper); font-size: 13px;
  }
</style>
</head>
<body>
<main class="stage">
  <section class="card card-front" aria-label="Card front">
    <svg class="front-swoosh" width="525" height="300" viewBox="0 0 525 300" aria-hidden="true">
      <path d="M0,0 H275 L255,40 Q110,58 0,140 Z" fill="var(--green)"/>
      <path d="M0,140 Q110,58 255,40 L250,100 Q100,98 0,168 Z" fill="var(--blue)"/>
    </svg>
    <div class="holder">
      <p class="holder-name">Dario Menteval</p>
      <p class="holder-title">Principal</p>
    </div>
    <div class="brand brand-front"><span class="brand-dot"></span>velbrix</div>
    <div class="contact">
      <p>418 Harlow Avenue</p>
      <p>Ridgeton, IL 60420</p>
      <div class="contact-gap"></div>
      <p class="contact-line">555.214.7730
        <svg class="contact-icon" viewBox="0 0 12 12"><rect width="12" height="12" rx="2" fill="var(--green)"/><path d="M3,3 L5,3 L5.5,5 L4.5,5.6 Q5.5,7 6.6,7.5 L7.1,6.6 L9,7 L9,9 Q4,9 3,3 Z" fill="#fff"/></svg></p>
      <p class="contact-line">555.214.7731
        <svg class="contact-icon" viewBox="0 0 12 12"><rect width="12" height="12" rx="2" fill="var(--green)"/><rect x="3" y="4" width="6" height="4" fill="#fff"/></svg></p>
      <p class="contact-line">dario@velbrix.com
        <svg class="contact-icon" viewBox="0 0 12 12"><rect width="12" height="12" rx="2" fill="var(--green)"/><path d="M2.5,3.5 H9.5 V8.5 H2.5 Z M2.5,3.5 L6,6.5 L9.5,3.5" fill="none" stroke="#fff" stroke-width="1"/></svg></p>
      <p class="contact-web">www.velbrix.com</p>
    </div>
  </section>
  <section class="card card-back" aria-label="Card back">
    <div class="brand brand-back"><span class="brand-dot"></span>velbrix</div>
    <p class="back-web">www.yourwebsite.com</p>
  </section>
</main>
</body>
</html>
```